Redesign of a facility management homepage

We need a redesign/an improved design of the facility management homepage (http://www.kolvenhaus-drefling.de/).
This websites offers detailed information on the "About us" as company, the "Services" provided and special information on facility and strata management. We would like to keep the structure of the website.
We need ideas/designs how this website could look more modern and confidential and appealing/pleasant for visitors at the same time and not losing the main purpose of information distribution.
The green color must be used since this is the basic color from our logo.
The blue in the background of the logo ist optional. So feel to use it or not.
We need no coding only design (.psd or as .ai)
Industry/Entity Type
It Company
Look and feel
Each slider illustrates characteristics of the customer's brand and the style your logo design should communicate.

```html
<!DOCTYPE html>
<html lang="de">
<head>
<meta charset="utf-8">
<title>Kolvenhaus GmbH – Facility Management</title>
<link rel="stylesheet" href="https://fonts.googleapis.com/css2?family=Arimo:wght@400;600;700&family=Tinos:ital@1&display=swap">
<style>
:root{
  --green:#2e8b47;
  --green-dark:#236f38;
  --green-text:#3a9a4e;
  --mint:#eefbe9;
  --mint-soft:#e6fcdc;
  --bar:#333333;
  --white:#ffffff;
  --ink:#222222;
}
*{margin:0;padding:0;box-sizing:border-box}
html,body{width:1137px;height:1200px;overflow:hidden}
body{position:relative;background:var(--white);font-family:"Arimo",Arial,sans-serif;color:var(--ink)}
.topbar{position:absolute;left:0;top:0;width:1137px;height:25px;background:var(--bar);color:#eee;font-size:13px;display:flex;align-items:center;padding:0 10px}
.topbar .tagline{font-family:"Tinos",serif;font-style:italic;font-size:14px;letter-spacing:.3px}
.topbar .contact{margin-left:auto;display:flex;gap:22px;align-items:center}
.topbar .contact span{display:flex;align-items:center;gap:6px}
.header-bg{position:absolute;left:0;top:25px;width:1137px;height:191px;background:var(--mint)}
.stage-bg{position:absolute;left:0;top:216px;width:1137px;height:392px;background:var(--mint-soft)}
.brand{position:absolute;left:36px;top:68px;display:flex;align-items:center;gap:10px;font-weight:700;font-size:30px;color:var(--green)}
.brand i{display:block;width:18px;height:18px;background:var(--green)}
.nav{position:absolute;left:287px;top:80px;width:840px;height:45px}
.nav a{position:absolute;top:0;height:45px;line-height:42px;font-size:18px;color:var(--green-text);text-decoration:none;font-weight:600}
.nav .active{left:0;width:151px;background:var(--green);color:var(--white);text-align:center;font-weight:400}
.subnav{position:absolute;left:287px;top:125px;width:839px;height:31px;background:var(--green);display:flex;align-items:center;color:var(--white);font-size:16px}
.subnav span{position:absolute}
.slider{position:absolute;left:9px;top:156px;width:1117px;height:424px;border:5px solid var(--green);background:var(--white)}
.slider .photo{position:absolute;inset:2px;background:linear-gradient(180deg,#c9a671 0%,#9c8d6a 25%,#e9eef0 45%,#d8dde0 70%,#8a8174 100%)}
.slider .caption{position:absolute;left:2px;right:2px;bottom:2px;height:92px;background:rgba(235,235,235,.85);font-size:55px;color:var(--green);padding:10px 14px}
.arrow{position:absolute;top:347px;width:46px;height:46px;background:rgba(46,139,71,.85);border-radius:5px;display:flex;align-items:center;justify-content:center}
.cards{position:absolute;left:0;top:624px;width:1137px}
.card{position:absolute;top:0;width:266px}
.card .frame{height:205px;border:3px solid #3e9a55;box-shadow:0 2px 6px rgba(0,0,0,.3);padding:4px;position:relative;background:var(--white)}
.card .pic{width:100%;height:100%}
.card .label{position:absolute;left:4px;right:4px;bottom:4px;height:40px;background:rgba(46,139,71,.85);color:var(--white);font-size:16px;display:flex;align-items:center;justify-content:center;letter-spacing:.3px}
.card p{margin-top:14px;text-align:center;font-size:12.5px;line-height:24px;letter-spacing:.3px}
.more{position:absolute;height:20px;padding:0 10px;border-radius:10px;background:#e2f5e2;font-size:12.5px;color:#333;display:flex;align-items:center;gap:6px}
.footer{position:absolute;left:0;top:991px;width:1137px;height:209px;background:var(--green);color:var(--white);font-weight:600;letter-spacing:.4px}
.footer::after{content:"";position:absolute;left:0;bottom:0;width:100%;height:10px;background:var(--green-dark)}
.footer .col{position:absolute;top:26px}
.footer h3{font-size:19px;font-weight:700;margin-bottom:12px}
.footer li{list-style:none;font-size:15px;line-height:29px}
.footer .loc li{line-height:27px}
.footer u{text-underline-offset:3px}
</style>
</head>
<body>
<div class="topbar">
  <span class="tagline">Kolvenhaus Büro- und Hausmeisterservice GmbH Drefling &nbsp;&nbsp;&nbsp; Ihr Partner vor Ort.</span>
  <div class="contact">
    <span><svg width="10" height="12" viewBox="0 0 10 12"><path d="M2 0h2l1 3-1.5 1a6 6 0 0 0 2.5 4l1.2-1.3L10 8v2l-1.5 1.5C5 12 0 6 .5 1.5Z" fill="#eee"/></svg>0 41 53 / 72 40 18</span>
    <span><svg width="16" height="11" viewBox="0 0 16 11"><rect x=".5" y=".5" width="15" height="10" fill="none" stroke="#eee"/><path d="M.5.5 8 6l7.5-5.5" fill="none" stroke="#eee"/></svg>info@kolvenhaus-drefling.de</span>
  </div>
</div>
<div class="header-bg"></div>
<div class="stage-bg"></div>

<div class="brand"><i></i>Kolvenhaus</div>

<nav class="nav">
  <a class="active">Wir über uns</a>
  <a style="left:199px">Gebäudemanagement</a>
  <a style="left:472px">Gebäudeverwaltung</a>
  <a style="left:714px">Vermietung</a>
</nav>
<div class="subnav">
  <span style="left:35px">Kolvenhaus GmbH</span>
  <span style="left:179px">Team</span>
  <span style="left:285px">Geschichte</span>
  <span style="left:428px">Einsatzgebiet</span>
</div>

<section class="slider">
  <div class="photo" role="img" aria-label="Fuhrpark weißer Firmentransporter vor einem Bürogebäude im Herbst"></div>
  <div class="caption">Kolvenhaus GmbH</div>
</section>
<div class="arrow" style="left:23px"><svg width="16" height="30" viewBox="0 0 16 30"><path d="M14 2 2 15l12 13" fill="none" stroke="#fff" stroke-width="2.5"/></svg></div>
<div class="arrow" style="left:1063px"><svg width="16" height="30" viewBox="0 0 16 30"><path d="M2 2l12 13L2 28" fill="none" stroke="#fff" stroke-width="2.5"/></svg></div>

<section class="cards">
  <div class="card" style="left:43px">
    <div class="frame"><div class="pic" role="img" aria-label="Gartengeräte wie Aufsitzmäher und Rasenmäher" style="background:linear-gradient(180deg,#2f5a2a,#8a3a32 60%,#6b6b6b)"></div><div class="label">Garten – Außenanlagen</div></div>
    <p>Die aufgeführte Auswahl an Geräten<br>verdeutlichen die sehr gute Ausstattung<br>der Kolvenhaus.</p>
  </div>
  <div class="card" style="left:434px">
    <div class="frame"><div class="pic" role="img" aria-label="Reinigungsgeräte und Hochdruckreiniger" style="background:linear-gradient(180deg,#2f4f2a,#6f7a5e 60%,#cfcfc0)"></div><div class="label">Reinigung Kehrdienst</div></div>
    <p>Die Mitarbeiter der Kolvenhaus führen auch<br>Reinigungen und Kehrdienste<br>gemeinschaftlicher Bereiche<br>eines Anwesens</p>
  </div>
  <div class="card" style="left:829px">
    <div class="frame"><div class="pic" role="img" aria-label="Mitarbeiter beim Schneeräumen im Winter" style="background:linear-gradient(180deg,#d9c05a,#e7eaee 45%,#cfd5dc)"></div><div class="label">Winterdienst</div></div>
    <p>Bei Glätte wird Splitt, Splitt-Salz-Gemisch<br>oder Salz gestreut.</p>
  </div>
</section>
<div class="more" style="left:214px;top:909px">Learn more <svg width="5" height="8"><path d="M0 0l5 4-5 4z" fill="#2e8b47"/></svg></div>
<div class="more" style="left:603px;top:945px">Learn more <svg width="5" height="8"><path d="M0 0l5 4-5 4z" fill="#2e8b47"/></svg></div>
<div class="more" style="left:997px;top:909px">Learn more <svg width="5" height="8"><path d="M0 0l5 4-5 4z" fill="#2e8b47"/></svg></div>

<footer class="footer">
  <div class="col" style="left:48px">
    <h3>Quick Access</h3>
    <ul><li>Störung online melden</li><li>Kontakt</li><li>Links</li><li>Impressum</li></ul>
  </div>
  <div class="col loc" style="left:394px">
    <h3>Location</h3>
    <ul><li>Kolvenhaus Büro- und Hausmeisterservice GmbH</li><li>Lindenplatz 14-16 in 21493 Drefling</li><li>vertreten durch Frau Helga Brandeis,</li><li>Geschäftsführerin</li><li>AG Lüneburg, HR.Nr.: HRB 48217</li></ul>
  </div>
  <div class="col" style="left:819px">
    <h3>Contact Us</h3>
    <ul><li>Tel.: 0 41 53 / 72 40 18</li><li>Fax: 0 41 53 / 72 40 26</li><li>Mail: info@kolvenhaus-drefling.de</li><li><u>Kontaktformular</u></li></ul>
  </div>
</footer>
</body>
</html>
```